Management consultant needs to update look of website

Currently I have a great word press website but it needs an updated look. I have new text for the site in the attached word document. I also have a list of websites whose design, look, and organization i like as a guide for the designer. The final design should be simple, strong, clear, and project the idea that my brand is a powerful authority in this space. Current site = www.corvelstrategy.example

Target Market(s)

company owners / executives

Industry/Entity Type

Management Consulting

Number of Pages Required

3 page

Font styles to use
Serif

Colors

Designer to choose colors to be used in the design.

Requirements
Must have
• a simple and clear design and message. professional look. easy navigation. responsive to mobile devices. an easily implemented wordpress theme OR squarespace. use of my logo colors. though I am open to changing to a deep navy or charcoal logo image. source file uploaded.
Nice to have
• i like the cover photo and logo watermark on my current homepage. i like the google map with my logo on the current contact page. i like the animation as well. a great blend of the current site and something that is more seamless.

```html
<!DOCTYPE html>
<html lang="en">
<head>
<meta charset="utf-8">
<title>Corvel Strategy — Website Design</title>
<link rel="stylesheet" href="https://fonts.googleapis.com/css2?family=Open+Sans:wght@400;600;700;800&family=Gelasio:ital,wght@0,400;0,700;1,400&display=swap">
<style>
:root{
  --stage:#d8d8d3;
  --paper:#ffffff;
  --charcoal:#2a2a2a;
  --ink:#333333;
  --muted:#7a7a7a;
  --gold:#99680f;
  --gold-light:#d9b45a;
  --sand:#efe7d6;
  --tile:#8f8f8f;
  --blue:#1c7fd6;
  --blue-dark:#0d5fb0;
}
*{box-sizing:border-box;margin:0;padding:0}
html,body{width:1200px;height:901px;overflow:hidden;background:var(--stage)}
body{font-family:"Gelasio",Georgia,serif;color:var(--ink)}
.board{display:flex;gap:22px;padding:20px 24px;height:901px}
.page{flex:1;min-width:0;background:var(--paper);height:861px;overflow:hidden;box-shadow:0 6px 18px rgba(0,0,0,.18);display:flex;flex-direction:column}

/* nav */
.nav{flex:none;display:flex;align-items:center;justify-content:space-between;padding:8px 12px;background:var(--charcoal);color:#fff}
.brand{display:flex;align-items:center;gap:6px;font-family:"Open Sans",Arial,sans-serif;font-size:9px;font-weight:600;letter-spacing:.5px}
.brand-dot{width:12px;height:12px;border-radius:50%;background:var(--gold-light)}
.nav-links{display:flex;gap:9px;font-family:"Open Sans",Arial,sans-serif;font-size:6.5px;text-transform:uppercase;letter-spacing:.6px;color:#ddd}

/* home hero */
.hero{flex:none;height:212px;background:linear-gradient(180deg,#5d5d5d 0%,#2b2b2b 60%,#181818 100%);position:relative;color:#fff;text-align:center;padding-top:30px}
.hero h1{font-family:"Gelasio",serif;font-weight:400;font-size:17px}
.hero .sub{font-size:7px;color:#ccc;margin-top:3px}
.btn{display:inline-block;background:var(--gold-light);color:#2a2a2a;font-family:"Open Sans",Arial,sans-serif;font-size:6.5px;font-weight:700;padding:4px 12px;border-radius:10px;text-transform:uppercase;letter-spacing:.5px}
.hero .btn{margin-top:7px}
.hero-cards{position:absolute;left:12px;right:12px;bottom:12px;display:flex;gap:10px}
.hero-card{flex:1;background:rgba(0,0,0,.55);padding:8px;text-align:left}
.hero-card h2{font-family:"Open Sans",Arial,sans-serif;font-size:10px;font-weight:600}
.hero-card p{font-size:6px;color:#ccc;margin:3px 0 5px;line-height:1.35}
.gold-band{flex:none;height:8px;background:var(--gold)}

.section{padding:10px 14px;text-align:center}
.section h3{font-family:"Open Sans",Arial,sans-serif;font-size:11px;font-weight:700;text-transform:uppercase;letter-spacing:.6px;color:var(--charcoal);margin-bottom:5px}
.section h3.plain{text-transform:none}
.body-text{font-size:7px;line-height:1.45;color:var(--ink);text-align:left}
.small-text{font-size:6px;line-height:1.4;color:var(--ink)}
.section .btn{margin-top:6px}

.quotes{display:flex;gap:8px;text-align:left}
.quote{flex:1;font-size:5.8px;line-height:1.4;color:var(--muted)}
.quote .who{display:flex;align-items:center;gap:4px;margin-top:4px;color:var(--ink);font-weight:700}
.avatar{width:10px;height:10px;border-radius:50%;background:#b9b2a6;flex:none}
.dots{display:flex;justify-content:center;gap:3px;margin-top:6px}
.dots span{width:4px;height:4px;border-radius:50%;background:#555}

.logo-grid{display:grid;grid-template-columns:repeat(6,1fr);gap:4px;padding:0 6px}
.logo-grid div{height:30px;background:var(--tile)}

.unlock{flex:none;background:var(--gold);color:#fff;padding:10px 14px;display:flex;gap:10px;align-items:center;margin-top:8px}
.unlock-copy{flex:1.1}
.unlock-copy h4{font-family:"Open Sans",Arial,sans-serif;font-size:9px;font-weight:800;line-height:1.2}
.unlock-copy h4 small{display:block;font-weight:400;font-size:8px}
.unlock-copy p{font-size:6px;margin-top:4px;line-height:1.35;color:#f3e6c8}
.form{flex:1;display:flex;flex-direction:column;gap:4px}
.form .title{font-family:"Open Sans",Arial,sans-serif;font-size:11px;font-weight:800;letter-spacing:1px;text-align:center}
.field{background:#fff;color:#555;font-family:"Open Sans",Arial,sans-serif;font-size:6px;padding:3px 5px}
.submit{border:1px solid #fff;font-family:"Open Sans",Arial,sans-serif;font-size:6.5px;text-align:center;padding:3px}

.footer{flex:1;background:linear-gradient(180deg,#d8ccb3,#b9aa8c);display:flex;flex-direction:column;align-items:center;justify-content:center;gap:6px;font-family:"Open Sans",Arial,sans-serif;font-size:6px;color:#3a3020}
.social{display:flex;gap:6px}
.social span{width:14px;height:14px;border-radius:50%;background:var(--gold)}

/* about */
.about-hero{flex:none;height:210px;background:linear-gradient(160deg,#d9c9a8,#b59b6f 55%,#8c7653)}
.blue-strip{flex:none;height:6px;background:var(--blue)}
.about-body{flex:none;background:var(--sand);padding:10px 14px}
.portrait-row{display:flex;gap:10px;align-items:center}
.portrait{width:48px;height:48px;border-radius:50%;border:3px solid #fff;background:linear-gradient(135deg,#c8b49a,#8e7660);flex:none}
.services-head{flex:none;display:flex;align-items:center;padding:8px 14px;gap:10px}
.services-head h3{font-family:"Open Sans",Arial,sans-serif;font-size:11px;font-weight:700;letter-spacing:.6px;text-transform:uppercase;flex:1}
.chess{width:150px;height:60px;background:linear-gradient(90deg,#e6ddd0,#a89880)}

/* hexagon panels */
.hex-row{flex:none;display:flex;gap:6px;padding:0 12px 8px}
.step{flex:1;min-width:0;height:118px;background:linear-gradient(135deg,var(--blue),var(--blue-dark));clip-path:polygon(50% 0,100% 20%,100% 100%,0 100%,0 20%);color:#fff;padding:26px 7px 6px}
.step.short{height:100px}
.step h5{font-family:"Open Sans",Arial,sans-serif;font-size:8px;font-weight:700}
.step p{font-size:5.8px;line-height:1.4;margin-top:4px;color:#e3efff}
.hex-photo{flex:1;min-width:0;height:100px;align-self:flex-end}
.photo-mosaic{background:linear-gradient(135deg,#b9a582,#6f5b3f)}
.photo-climb{background:linear-gradient(135deg,#b5564a,#6e3a33)}

.icon-row{flex:none;display:flex;align-items:flex-start;gap:8px;padding:6px 14px 8px}
.icon{width:26px;height:26px;border-radius:50%;background:#fff;border:2px solid var(--blue);flex:none;display:flex;align-items:center;justify-content:center}
.icon span{width:10px;height:10px;border-radius:50%;background:var(--blue)}
.icon-copy{flex:1}
.icon-copy h6{font-family:"Open Sans",Arial,sans-serif;font-size:8px;font-weight:700;color:var(--charcoal);margin-bottom:2px}
.icon-copy .btn{margin-top:4px;padding:3px 10px;font-size:6px}

.svc-hero{flex:none;height:70px;background:linear-gradient(180deg,#e9e4db,#b8ab96)}
.mini-quotes{flex:1.2;min-width:0;display:flex;flex-direction:column;gap:5px;align-self:flex-end}
.mini-quote{background:#f5f5f5;padding:5px;font-size:5.6px;line-height:1.35;color:var(--muted)}
.mini-quote .who{display:flex;align-items:center;gap:4px;margin-top:3px;color:var(--ink);font-weight:700}

.contact{margin-top:auto;flex:none;display:flex}
.contact-info{flex:1;background:var(--gold-light);padding:12px;font-family:"Open Sans",Arial,sans-serif;font-size:7px;line-height:1.6;color:#2a2a2a}
.contact-info strong{display:block;font-size:9px}
.map{flex:1.2;height:120px;background:linear-gradient(135deg,#9a9a9a,#5c5c5c)}
</style>
</head>
<body>
<main class="board">

  <!-- Home -->
  <section class="page">
    <nav class="nav">
      <div class="brand"><span class="brand-dot"></span>Corvel Strategy</div>
      <div class="nav-links"><span>Home</span><span>About</span><span>Services</span><span>Contact</span></div>
    </nav>
    <header class="hero" role="img" aria-label="Black and white city skyline cover photograph">
      <h1>Great Companies Succeed</h1>
      <p class="sub">by developing and inspiring their people</p>
      <span class="btn">Learn more</span>
      <div class="hero-cards">
        <div class="hero-card"><h2>Learn to Inspire</h2><p>Practical guidance that helps leaders connect with and motivate their teams.</p><span class="btn">Read more</span></div>
        <div class="hero-card"><h2>Management Workshops</h2><p>Hands-on sessions that build stronger managers and clearer direction.</p><span class="btn">Read more</span></div>
      </div>
    </header>
    <div class="gold-band"></div>
    <div class="section">
      <h3 class="plain">What we do?</h3>
      <p class="body-text">It's no secret that long-term business success requires a smart investment in the right people for your company. And yet, knowing how to cultivate a strong staff and keep them focused on the road ahead can be challenging. Dr. Elena Marsh and her team help business owners, leaders, and HR teams understand how to identify, develop, and retain talented professionals who can take your success to the next level.</p>
      <span class="btn">Our services</span>
    </div>
    <div class="section">
      <h3>Testimonials</h3>
      <div class="quotes">
        <div class="quote">Her workshops gave our managers a clear plan and renewed energy for the year ahead.<div class="who"><span class="avatar"></span>Mark Ellis, CEO</div></div>
        <div class="quote">We saw real change in retention within months. A trusted partner for our leaders.<div class="who"><span class="avatar"></span>Anne Ruiz, HR Lead</div></div>
        <div class="quote">Insightful, direct and practical. Our executive team works together far better now.<div class="who"><span class="avatar"></span>Paul Grant, Owner</div></div>
      </div>
      <div class="dots"><span></span><span></span><span></span><span></span></div>
    </div>
    <div class="section" style="padding-top:2px">
      <h3>Logos</h3>
      <div class="logo-grid">
        <div></div><div></div><div></div><div></div><div></div><div></div>
        <div></div><div></div><div></div><div></div><div></div><div></div>
      </div>
    </div>
    <div class="unlock">
      <div class="unlock-copy">
        <h4>LEARN TO INSPIRE EMPLOYEES<small>and Unlock Their Maximum Potential</small></h4>
        <p>Struggling to connect with today's employees? Find a better way to lead them and become the very best leader possible.</p>
      </div>
      <div class="form">
        <div class="title">UNLOCK</div>
        <div class="field">John Smith</div>
        <div class="field">••••••••••••</div>
        <div class="submit">Download Free Information</div>
      </div>
    </div>
    <footer class="footer">
      <div class="social"><span></span><span></span><span></span><span></span><span></span></div>
      <span>www.corvelstrategy.example</span>
    </footer>
  </section>

  <!-- About -->
  <section class="page">
    <nav class="nav">
      <div class="brand"><span class="brand-dot"></span>Corvel Strategy</div>
      <div class="nav-links"><span>Home</span><span>About</span><span>Services</span><span>Contact</span></div>
    </nav>
    <div class="about-hero" role="img" aria-label="Warm-toned photograph of a team meeting in a bright office"></div>
    <div class="blue-strip"></div>
    <div class="about-body">
      <div class="section" style="padding:0 0 6px"><h3>About</h3></div>
      <p class="body-text">Dr. Elena Marsh is a business consultant, keynote speaker and executive coach specializing in workplace culture, leadership development and organizational growth. She is the founder of Corvel Strategy and an instructor of executive education at Halden Business School.</p>
      <div class="portrait-row" style="margin-top:6px">
        <div class="portrait" role="img" aria-label="Portrait photograph of the consultant"></div>
        <p class="body-text">She has spent years helping companies of every size build teams that stay, grow and perform. Her approach blends research with clear, practical steps that leaders can apply right away.</p>
      </div>
      <p class="body-text" style="margin-top:6px">Her concentration in organizational behavior and social psychology has led to published work in leading journals. She earned her doctorate at Westbrook University and now works with owners and executives to give you sound advice and actionable data to help you lead.</p>
    </div>
    <div class="services-head">
      <h3>Services</h3>
      <div class="chess" role="img" aria-label="Photograph of chess pieces on a board"></div>
    </div>
    <div class="icon-row">
      <div class="icon"><span></span></div>
      <div class="icon-copy">
        <p class="body-text">Business growth, even in the beginning, comes down to people. We help you find them, develop them and keep them, so your company is ready for the next stage.</p>
        <span class="btn">Learn more</span>
      </div>
    </div>
    <div class="hex-row">
      <div class="step"><h5>Step 1. Discovery</h5><p>A baseline survey and in-depth interviews reveal the current culture and where your people need support.</p></div>
      <div class="step"><h5>Step 2. Strategy</h5><p>We build a complete plan to raise engagement, retention and leadership at all levels of your firm.</p></div>
      <div class="step"><h5>Step 3. Results</h5><p>We guide the rollout, coach your leaders and measure progress so the change lasts.</p></div>
    </div>
    <div class="icon-row">
      <div class="icon"><span></span></div>
      <div class="icon-copy">
        <h6>Management Workshops</h6>
        <p class="body-text">Bringing an expert in-house to train your managers gives them the tools to lead with confidence and clarity.</p>
      </div>
    </div>
  </section>

  <!-- Services -->
  <section class="page">
    <nav class="nav">
      <div class="brand"><span class="brand-dot"></span>Corvel Strategy</div>
      <div class="nav-links"><span>Home</span><span>About</span><span>Services</span><span>Contact</span></div>
    </nav>
    <div class="svc-hero" role="img" aria-label="Photograph of chess pieces in soft light"></div>
    <div class="hex-row" style="padding-top:8px">
      <div class="step short"><h5>Team Assessment</h5><p>We measure how your people work together today.</p></div>
      <div class="step short"><h5>Culture Review</h5><p>Clear insight into values, habits and morale.</p></div>
      <div class="hex-photo photo-mosaic" role="img" aria-label="Photograph of a tiled mosaic in warm brown tones"></div>
    </div>
    <div class="icon-row">
      <div class="icon"><span></span></div>
      <div class="icon-copy">
        <h6>Management Workshops</h6>
        <p class="small-text">Interactive sessions that give managers practical skills to guide, motivate and grow their teams.</p>
        <span class="btn">Learn more</span>
      </div>
    </div>
    <div class="hex-row">
      <div class="step short"><h5>Leadership Skills</h5><p>Build trust, set direction and lead change.</p></div>
      <div class="step short"><h5>Communication</h5><p>Clear feedback and better team dialogue.</p></div>
      <div class="hex-photo photo-climb" role="img" aria-label="Photograph of a climber on a red rock face"></div>
    </div>
    <div class="icon-row">
      <div class="icon"><span></span></div>
      <div class="icon-copy">
        <h6>Executive Coaching</h6>
        <p class="small-text">One-on-one coaching that helps owners and executives sharpen focus and lead with purpose.</p>
        <span class="btn">Learn more</span>
      </div>
    </div>
    <div class="hex-row">
      <div class="step short"><h5>Goal Setting</h5><p>Turn vision into clear, lasting priorities.</p></div>
      <div class="mini-quotes">
        <div class="mini-quote">Coaching changed how I run my leadership team.<div class="who"><span class="avatar"></span>Lisa Hart, COO</div></div>
        <div class="mini-quote">Focused, honest and very effective advice.<div class="who"><span class="avatar"></span>Tom Reyes, CEO</div></div>
      </div>
    </div>
    <div class="contact">
      <div class="contact-info">
        <strong>Contact</strong>
        Corvel Strategy<br>
        210 Harbor Lane, Suite 4<br>
        Phone: (555) 014-2290<br>
        www.corvelstrategy.example
      </div>
      <div class="map" role="img" aria-label="Street map showing the office location"></div>
    </div>
  </section>

</main>
</body>
</html>
```